Business card for Property Management consultant

I need a business card for my business LX Vantage - I consult to real estate agents to improve the performance of their Property Management departments (rental houses management). The card needs to be very professional looking, incorporating our logo and my photo plus the line "Develop your Rent Roll to Perform"

Target Market(s)

Real Estate business owners

Industry/Entity Type

Business Consultant

Contact Information for Business Card

Business name - LX Vantage (logo uploaded)
My Name : Marcia Kellaway -
Title : Property Management Consultant

Develop your Rent Roll to perform

Phone : +61 438592716
email : marcia@lxvantage.com.au
website ; www.lxvantage.com.au

Requirements
Must have
• Logo
• My photo
• Very corporate / professional look

```html
<!DOCTYPE html>
<html lang="en">
<head>
<meta charset="utf-8">
<title>LX Vantage – Business Card</title>
<link rel="stylesheet" href="https://fonts.googleapis.com/css2?family=Poppins:wght@500;600;700&family=Roboto:wght@400;500&display=swap">
<style>
  :root {
    --bg: #d9d9db;
    --card: #ffffff;
    --blue: #2459a8;
    --gold: #c8931f;
    --ink: #141414;
    --text: #2b2b2b;
    --photo-a: #7a3a26;
    --photo-b: #d9a48a;
  }
  * { margin: 0; padding: 0; box-sizing: border-box; }
  html, body { width: 1200px; height: 1200px; overflow: hidden; }
  body {
    background: var(--bg);
    display: flex; align-items: center; justify-content: center;
    font-family: "Roboto", sans-serif;
  }
  .card {
    position: relative;
    width: 1000px; height: 571px;
    background: var(--card);
    border-radius: 40px;
    overflow: hidden;
    box-shadow: 0 10px 30px rgba(0,0,0,0.12);
  }
  .band {
    position: absolute; left: 0; top: 0;
    width: 100%; height: 78px;
    background: var(--blue);
    border-bottom: 9px solid var(--gold);
  }
  .tagline {
    position: absolute; left: 52px; top: 34px;
    color: #fff;
    font-family: "Poppins", sans-serif;
    font-weight: 700; font-size: 18px;
    letter-spacing: 2px;
  }
  .photo {
    position: absolute; left: 565px; top: 22px;
    width: 250px; height: 250px;
    border-radius: 50%;
    border: 11px solid var(--gold);
    background: radial-gradient(circle at 50% 40%, var(--photo-b) 0%, var(--photo-b) 35%, var(--photo-a) 70%, var(--blue) 100%);
  }
  .name {
    position: absolute; left: 95px; top: 160px;
    color: var(--blue);
    font-family: "Poppins", sans-serif;
    font-weight: 700; font-size: 46px;
    letter-spacing: -0.5px;
  }
  .title {
    position: absolute; left: 118px; top: 228px;
    color: var(--text);
    font-size: 20px; font-weight: 500;
    letter-spacing: 2.5px;
  }
  .contacts {
    position: absolute; left: 235px; top: 400px;
    list-style: none;
  }
  .contacts li {
    display: flex; align-items: center; gap: 16px;
    font-size: 18px; letter-spacing: 2px;
    color: var(--text);
    height: 32px;
  }
  .contacts svg { width: 20px; height: 20px; flex: none; }
  .brand {
    position: absolute; left: 630px; top: 320px;
    display: flex; align-items: center; gap: 18px;
  }
  .brand-mark {
    width: 44px; height: 44px;
    background: var(--blue);
  }
  .brand-name {
    font-family: "Poppins", sans-serif;
    font-weight: 600; font-size: 50px;
    color: var(--ink);
  }
</style>
</head>
<body>
  <div class="card">
    <div class="band"></div>
    <div class="tagline">Develop your Rent Roll to perform</div>
    <div class="photo" role="img" aria-label="Portrait photo of Marcia Kellaway"></div>

    <div class="name">Marcia Kellaway</div>
    <div class="title">property management consultant</div>

    <ul class="contacts">
      <li>
        <svg viewBox="0 0 20 20" aria-hidden="true"><rect x="4" y="2" width="12" height="16" rx="2" fill="none" stroke="#2459a8" stroke-width="2"/><circle cx="10" cy="15" r="1" fill="#2459a8"/></svg>
        +61 438592716
      </li>
      <li>
        <svg viewBox="0 0 20 20" aria-hidden="true"><rect x="2" y="4" width="16" height="12" fill="none" stroke="#2459a8" stroke-width="2"/><path d="M2 5 L10 11 L18 5" fill="none" stroke="#2459a8" stroke-width="2"/></svg>
        marcia@lxvantage.com.au
      </li>
      <li>
        <svg viewBox="0 0 20 20" aria-hidden="true"><circle cx="10" cy="10" r="8" fill="#2459a8"/><path d="M2 10 H18 M10 2 C6 6 6 14 10 18 M10 2 C14 6 14 14 10 18" fill="none" stroke="#fff" stroke-width="1.2"/></svg>
        www.lxvantage.com.au
      </li>
    </ul>

    <div class="brand">
      <span class="brand-mark"></span>
      <span class="brand-name">LX Vantage</span>
    </div>
  </div>
</body>
</html>
```